Amber Lark Prints

wall art that with words that inspire and can uplift people in their homes in times when they are down. An ever present presence to inspire that the subconscious takes in and subliminally feeds the home owner with positivity. Quotes... 1)In the morning, devour the prey, in the evening, divide the spoils. 2)Your situation is not your potential, but your potential depends on how you see your situation. 3)It is never too late, if your still here, then there is still time. 4)Busy your mind with the concepts of harmony, health, peace, and good will, and wonders will happen in your life. 5), it is hard to think straight while going around in circles. 6)you have everything you need to proceed. thses are just a few examples.
I would like to have colourful backgrounds. I am starting a online poster store and need a series of beautifully designed words and colours or pictures that go together like a song and it's two elements of words and music.

Target Market(s)

Anybody with a wall that wants an uplifting presence

Industry/Entity Type

Wall art, home decor

Font styles to use
Serif
Other font styles liked:
• stencil, Dead kansas, newspaper headline styles

Requirements
Must have
• I got to put that on my wall, it's amazing
Nice to have
• I am a martial artist, music producer, writer, lyricist that likes to inspire, and I also appreciate nature and beauty, how this can be incorporated into an artistic expression would be ideal elements. maybe also the colours of

```html
<!DOCTYPE html>
<html lang="en">
<head>
<meta charset="utf-8">
<title>It Is Never Too Late</title>
<link rel="stylesheet" href="https://fonts.googleapis.com/css2?family=Jost:wght@500;600&display=swap">
<style>
  :root {
    --paper: #f1efea;
    --ink: #000000;
    --lime: #c9d334;
  }
  html, body {
    margin: 0;
    padding: 0;
    width: 1200px;
    height: 1200px;
    overflow: hidden;
    background: var(--paper);
  }
  .poster {
    display: block;
    width: 1200px;
    height: 1200px;
    background: var(--paper);
  }
  .quote-word {
    font-family: "Jost", sans-serif;
    font-weight: 600;
    fill: var(--ink);
  }
  .quote-word--accent { fill: var(--lime); }
  .quote-word--light { font-weight: 500; }
</style>
</head>
<body>
<svg class="poster" viewBox="0 0 1200 1200" xmlns="http://www.w3.org/2000/svg" role="img"
     aria-label="It is never too late if your still here then there is still time">
  <rect width="1200" height="1200" fill="var(--paper)"/>

  <!-- line one -->
  <text class="quote-word" x="14" y="199" font-size="263" textLength="1145" lengthAdjust="spacingAndGlyphs">IT IS NEVER</text>

  <!-- line two -->
  <text class="quote-word quote-word--light" x="36" y="346" font-size="174" textLength="682" lengthAdjust="spacingAndGlyphs">TOO LATE</text>

  <!-- line three -->
  <text class="quote-word" x="27" y="530" font-size="219" textLength="140" lengthAdjust="spacingAndGlyphs">IF</text>
  <text class="quote-word quote-word--accent" x="194" y="530" font-size="219" textLength="510" lengthAdjust="spacingAndGlyphs">YOUR</text>
  <text class="quote-word" x="741" y="530" font-size="219" textLength="444" lengthAdjust="spacingAndGlyphs">STILL</text>

  <!-- line four -->
  <text class="quote-word" x="14" y="797" font-size="366" textLength="728" lengthAdjust="spacingAndGlyphs">HERE</text>
  <text class="quote-word quote-word--light" x="764" y="681" font-size="180" textLength="379" lengthAdjust="spacingAndGlyphs">THEN</text>
  <text class="quote-word quote-word--accent" x="774" y="797" font-size="139" textLength="351" lengthAdjust="spacingAndGlyphs">THERE</text>

  <!-- line five -->
  <text class="quote-word quote-word--light" x="125" y="980" font-size="140" textLength="89" lengthAdjust="spacingAndGlyphs">IS</text>
  <text class="quote-word quote-word--accent" x="25" y="1111" font-size="140" textLength="268" lengthAdjust="spacingAndGlyphs">STILL</text>
  <text class="quote-word" x="220" y="1185" font-size="534" textLength="965" lengthAdjust="spacingAndGlyphs">TIME</text>
</svg>
</body>
</html>
```